13 Tavo - new website design project

Our company Tavo Electrical is developing a new lead generation website focused on Electrical, LED Lighting and Solar Power. We need a high converting website.

Example of our current website is www.tavoelectrical.com.au You can take content from this website for this new design. Our colours are red, black and white. For our new website we would like to promote Tavo, Bright Days Ahead. Please listen to the jingle.

The below link is the company jingle that we have developed.
http://www.tunecraftaudio.com.au/tav-tc-v1/

The key for this brief is to generate leads for Electrical, LED Lighting (for commercial) and Solar Power & Storage.

Target Market(s)

Business owners in Melbourne Victoria

Number of Pages Required

4 page

Colors
ec1f27
ffffff

Requirements
Must have
• This page must be clean, be in line with company branding and a high converting lead website.

```html
<!DOCTYPE html>
<html lang="en">
<head>
<meta charset="utf-8">
<title>Tavo Electrical</title>
<link href="https://fonts.googleapis.com/css2?family=Rajdhani:wght@400;500;600;700&family=Exo+2:ital,wght@1,900&display=swap" rel="stylesheet">
<style>
:root{
  --red:#c8161d;
  --brand-red:#ec1f27;
  --ink:#2e2e2e;
  --muted:#7a7a7a;
  --white:#ffffff;
  --nav-grey:#e4e4e4;
  --section-grey:#e8e8e8;
  --footer:#303239;
  --footer-line:#45474e;
  --seal-teal:#20424f;
  --seal-orange:#f39a1e;
}
*{box-sizing:border-box;margin:0;padding:0}
html,body{width:682px;height:1200px;overflow:hidden;background:var(--white)}
body{font-family:"Rajdhani",sans-serif;color:var(--ink);position:relative}

/* header */
.site-header{position:absolute;left:0;top:0;width:682px;height:45px;background:var(--white)}
.brand{position:absolute;left:92px;top:8px;display:flex;align-items:center;gap:5px}
.brand-dot{width:14px;height:14px;border-radius:50%;background:var(--red)}
.brand-name{font-weight:700;font-size:22px;color:var(--ink);line-height:1}
.brand-tag{position:absolute;left:100px;top:31px;font-size:7px;font-weight:600;color:var(--ink)}
.header-phone{position:absolute;left:540px;top:0;width:142px;height:45px;background:#ededed;clip-path:polygon(0 0,100% 0,100% 100%,0 100%,16% 50%)}
.header-phone .num{position:absolute;left:50px;top:8px;font-weight:700;font-size:26px;color:var(--red);line-height:1}
.header-phone svg{position:absolute;left:28px;top:12px}

/* nav */
.main-nav{position:absolute;left:0;top:45px;width:682px;height:33px;background:var(--nav-grey);border-bottom:3px solid var(--red)}
.main-nav a{position:absolute;top:0;height:33px;line-height:33px;font-size:6px;font-weight:600;color:#444;text-decoration:none;text-transform:uppercase}
.main-nav a.active{background:var(--red);color:var(--white);padding:0 8px}

/* hero */
.hero{position:absolute;left:0;top:81px;width:682px;height:144px}
.hero-photo{position:absolute;inset:0;background:linear-gradient(90deg,#2b3136 0%,#454d52 45%,#6b6c66 75%,#c7b79d 100%)}
.hero-title{position:absolute;left:52px;top:20px;font-family:"Exo 2",sans-serif;font-style:italic;font-weight:900;line-height:.88;transform:rotate(-4deg);transform-origin:left}
.hero-title .line1{display:block;font-size:32px;color:var(--red)}
.hero-title .line2{display:block;font-size:48px;color:var(--white)}

/* service */
.section-label{position:absolute;left:92px;top:250px;display:flex;align-items:baseline;gap:3px}
.section-label .idx{font-size:22px;font-weight:500;color:var(--ink)}
.section-label .name{font-size:12px;font-weight:500;color:var(--ink);border-bottom:1px solid var(--red)}
.service-photo{position:absolute;left:93px;top:284px;width:240px;height:140px;background:linear-gradient(135deg,#5a3a36,#b8402f 50%,#d9a341 80%,#c9b8a4)}
.service-copy{position:absolute;left:374px;top:282px;width:222px}
.service-copy h2{font-size:11px;font-weight:600;text-transform:uppercase;color:var(--ink)}
.service-copy h2 span{color:var(--red)}
.service-copy p{margin-top:4px;font-size:6.4px;line-height:12.8px;color:var(--muted)}
.service-copy h3{margin-top:8px;font-size:10px;font-weight:500}
.ticks{list-style:none;margin-top:5px}
.ticks li{display:flex;align-items:center;gap:5px;font-size:6.6px;height:13px;color:#444}

/* booking */
.booking{position:absolute;left:0;top:468px;width:682px;height:338px;background:var(--section-grey)}
.booking h2{position:absolute;left:0;width:682px;top:34px;text-align:center;font-size:18px;font-weight:700}
.booking h2 span{border-bottom:2px solid var(--red);padding-bottom:1px}
.field{position:absolute;background:#fdfbfb;border:1px solid #cfcfcf;font-size:7.5px;color:#999;padding:5px 9px}
.field.focus{border-color:#e3a2a4}
.submit{position:absolute;left:117px;top:278px;width:83px;height:20px;background:var(--red);color:var(--white);font-size:8px;font-weight:600;text-align:center;line-height:20px}

/* warranty */
.warranty{position:absolute;left:92px;top:878px;width:256px}
.warranty h2{font-size:11px;font-weight:600;text-transform:uppercase}
.warranty h3{margin-top:2px;font-size:9.5px;font-weight:600;color:var(--red)}
.warranty p{margin-top:5px;font-size:6px;line-height:12.8px;color:var(--muted)}
.guarantee-seal{position:absolute;left:394px;top:840px;width:198px;height:158px;border-radius:6px;background:radial-gradient(circle at 50% 50%,#f39a1e 0%,#8a6a3a 38%,#20424f 70%,#2a4e5b 100%)}

/* footer */
.site-footer{position:absolute;left:0;top:1033px;width:682px;height:167px;background:var(--footer)}
.footer-brand{position:absolute;left:126px;top:15px;display:flex;align-items:center;gap:4px}
.footer-brand .brand-name{color:var(--white);font-size:19px}
.footer-phone{position:absolute;left:126px;top:47px;display:flex;align-items:center;gap:3px;font-size:18px;font-weight:700;color:var(--red)}
.social{position:absolute;top:83px;width:18px;height:18px;border-radius:50%;background:#e6e6e6}
.social.first{background:#3a5a98}
.footer-col{position:absolute;color:var(--white)}
.footer-col h4{font-size:11.5px;font-weight:600;border-bottom:1px solid #6a6c72;padding-bottom:1px;display:inline-block}
.footer-col ul{list-style:none;margin-top:4px}
.footer-col li{font-size:7px;line-height:10.5px}
.quick li::before{content:"";display:inline-block;border-left:3px solid var(--white);border-top:2.5px solid transparent;border-bottom:2.5px solid transparent;margin-right:3px}
.pill{display:inline-block;height:7px;background:#4b67a6;margin-right:3px}
.copyright{position:absolute;left:0;top:116px;width:682px;height:51px;border-top:1px solid var(--footer-line);text-align:center;line-height:50px;font-size:7.5px;color:var(--white)}
.copyright span{color:var(--red)}
</style>
</head>
<body>

<header class="site-header">
  <div class="brand"><span class="brand-dot"></span><span class="brand-name">Tavo</span></div>
  <div class="brand-tag">Bright Days Ahead</div>
  <div class="header-phone">
    <svg width="18" height="16" viewBox="0 0 18 16"><path d="M1 6c2-5 14-5 16 0l-3 2-2-2H6L4 8z" fill="#1d1d1d"/><rect x="3" y="8" width="12" height="7" rx="2" fill="#1d1d1d"/><circle cx="9" cy="11.5" r="2" fill="#ededed"/></svg>
    <span class="num">13 7410</span>
  </div>
</header>

<nav class="main-nav">
  <a style="left:104px">Home</a>
  <a style="left:136px">Tavo Story</a>
  <a style="left:185px">Our Works</a>
  <a style="left:233px">Contact Us</a>
  <a class="active" style="left:455px">Electrical</a>
  <a style="left:506px">Led Lighting</a>
  <a style="left:554px">Solar Power</a>
</nav>

<section class="hero">
  <div class="hero-photo" role="img" aria-label="Smiling electrician in a yellow hard hat in front of an electrical switchboard"></div>
  <h1 class="hero-title"><span class="line1">NEED AN ELECTRICIAN?</span><span class="line2">COUNT ON US</span></h1>
</section>

<div class="section-label"><span class="idx">01</span><span class="name">ELECTRICAL</span></div>
<div class="service-photo" role="img" aria-label="Hand testing a switchboard with a yellow multimeter"></div>
<div class="service-copy">
  <h2><span>Tavo</span> offers save and safety</h2>
  <p>You can enjoy great discounts on energy usage charges, the freedom to move and more. So take a look at our energy plans. The choice is yours. We are always live to help you and light up your future is the main goal of our business</p>
  <h3>WE are available to provide more to your life</h3>
  <ul class="ticks">
    <li><svg width="9" height="8" viewBox="0 0 9 8"><rect x="0" y="1" width="7" height="7" fill="none" stroke="#c8161d"/><path d="M1.5 4l2 2L8.5 0.5" stroke="#c8161d" stroke-width="1.6" fill="none"/></svg>Melbourne wide</li>
    <li><svg width="9" height="8" viewBox="0 0 9 8"><rect x="0" y="1" width="7" height="7" fill="none" stroke="#c8161d"/><path d="M1.5 4l2 2L8.5 0.5" stroke="#c8161d" stroke-width="1.6" fill="none"/></svg>Quick reponse time</li>
    <li><svg width="9" height="8" viewBox="0 0 9 8"><rect x="0" y="1" width="7" height="7" fill="none" stroke="#c8161d"/><path d="M1.5 4l2 2L8.5 0.5" stroke="#c8161d" stroke-width="1.6" fill="none"/></svg>Electrical service provides by experienced electricion</li>
  </ul>
</div>

<section class="booking">
  <h2><span>BOOK ONLINE</span></h2>
  <div class="field focus" style="left:117px;top:92px;width:219px;height:20px">Name</div>
  <div class="field" style="left:345px;top:92px;width:219px;height:20px">Email</div>
  <div class="field" style="left:117px;top:122px;width:219px;height:20px">Phone</div>
  <div class="field" style="left:345px;top:122px;width:219px;height:20px">Address</div>
  <div class="field" style="left:117px;top:153px;width:448px;height:113px">Message</div>
  <div class="submit">Submit</div>
</section>

<div class="warranty">
  <h2>5-Year workmanship warranty</h2>
  <h3>Plus a minimum 1 year warranty on all products!</h3>
  <p>Great value for money, great service and reliability. These are the key foundations that we offer to our customers. All work is covered by a 5 year workmanship warranty and a minimum 1 year warranty on all products</p>
</div>
<div class="guarantee-seal" role="img" aria-label="Satisfaction guarantee 100% seal illustration"></div>

<footer class="site-footer">
  <div class="footer-brand"><span class="brand-dot"></span><span class="brand-name">Tavo</span></div>
  <div class="footer-phone">
    <svg width="16" height="14" viewBox="0 0 18 16"><path d="M1 6c2-5 14-5 16 0l-3 2-2-2H6L4 8z" fill="#111"/><rect x="3" y="8" width="12" height="7" rx="2" fill="#111"/></svg>13 7410
  </div>
  <span class="social first" style="left:126px"></span>
  <span class="social" style="left:150px"></span>
  <span class="social" style="left:173px"></span>

  <div class="footer-col quick" style="left:300px;top:26px">
    <h4>Some Quick Links</h4>
    <ul><li>Led Lighting</li><li>Solar Power</li><li>Electrical</li><li>Career</li></ul>
  </div>
  <div class="footer-col" style="left:484px;top:29px">
    <h4>Other</h4>
    <ul><li>Terms and Conditions</li><li>Privacy and policy</li></ul>
    <div style="margin-top:3px"><span class="pill" style="width:28px"></span><span class="pill" style="width:15px;background:#fff"></span><span class="pill" style="width:30px"></span></div>
  </div>

  <div class="copyright">© <span>Tavo</span> | Technologies | All rights reserved 2017</div>
</footer>

</body>
</html>
```